Harrow Collective
Chartered accountants & business advisors company seeks logo & business card design refresh - Financial Services
Simple
Derek Ostrander
Senior Project Accountant
PO Box 27 458 Wellington 6571
derek@harrowcollective.example.nz
harrowcollective.example.nz
Full Bleed Size (starting document size) 94 x 58 mm 1110 x 685 pixels * Finished artwork should use the full bleed dimensions for best results. Document Trim Size (final size after being cut) 91 x 55 mm 1075 x 650 pixels * Please be sure to keep all text within the safe margin. Resolution 300 DPI
Simple, perhaps solid colour with the web address (and logo etc)

```html
<!DOCTYPE html>
<html lang="en">
<head>
<meta charset="utf-8">
<title>Harrow Collective – Business Card</title>
<link rel="stylesheet" href="https://fonts.googleapis.com/css2?family=Montserrat:wght@400;500;600&display=swap">
<style>
  :root {
    --brand-blue: #2b7fcb;
    --ink-grey: #5a5f66;
    --card-white: #ffffff;
    --stage: #e9eaec;
  }
  * { box-sizing: border-box; margin: 0; padding: 0; }
  html, body {
    width: 1200px; height: 901px; overflow: hidden;
    background: var(--stage);
    font-family: "Montserrat", Arial, sans-serif;
  }
  .canvas {
    position: relative; width: 1200px; height: 901px;
    display: flex; align-items: center; justify-content: center; gap: 40px;
  }
  .card {
    position: relative; width: 540px; height: 326px;
    box-shadow: 0 6px 18px rgba(0,0,0,.12);
  }
  /* Back */
  .card-back { background: var(--brand-blue); color: var(--card-white); }
  .card-back .brand {
    position: absolute; left: 0; right: 0; top: 132px;
    display: flex; align-items: center; justify-content: center; gap: 12px;
  }
  .brand-dot {
    width: 16px; height: 16px; border-radius: 50%; background: currentColor;
  }
  .brand-name {
    font-weight: 500; font-size: 27px; letter-spacing: 2px; text-transform: uppercase;
  }
  .card-back .web {
    position: absolute; left: 0; right: 0; bottom: 34px; text-align: center;
    font-size: 13px; letter-spacing: 2px; opacity: .9;
  }
  /* Front */
  .card-front { background: var(--card-white); color: var(--brand-blue); }
  .card-front .brand {
    position: absolute; left: 30px; top: 132px;
    display: flex; align-items: center; gap: 9px;
  }
  .card-front .brand-name { font-size: 17px; letter-spacing: 1.5px; }
  .card-front .brand-dot { width: 12px; height: 12px; }
  .details {
    position: absolute; left: 300px; top: 78px; width: 225px;
    color: var(--ink-grey); font-size: 12px; line-height: 1.4;
  }
  .person-name { color: var(--brand-blue); font-weight: 600; font-size: 15px; }
  .person-title { font-size: 12px; margin-bottom: 14px; }
  .address { margin-bottom: 14px; }
  .contact-list { list-style: none; }
  .contact-list li { display: flex; align-items: center; gap: 7px; height: 18px; }
  .contact-list svg { width: 12px; height: 12px; flex: none; fill: var(--brand-blue); }
</style>
</head>
<body>
<main class="canvas">
  <section class="card card-back" aria-label="Card back">
    <div class="brand">
      <span class="brand-dot"></span>
      <span class="brand-name">Harrow Collective</span>
    </div>
    <p class="web">harrowcollective.example.nz</p>
  </section>

  <section class="card card-front" aria-label="Card front">
    <div class="brand">
      <span class="brand-dot"></span>
      <span class="brand-name">Harrow Collective</span>
    </div>
    <div class="details">
      <p class="person-name">Derek Ostrander</p>
      <p class="person-title">Senior Project Accountant</p>
      <p class="address">PO Box 27 458<br>Wellington 6571</p>
      <ul class="contact-list">
        <li><svg viewBox="0 0 12 12"><path d="M1 4c0-2 2-3 5-3s5 1 5 3l-2 1-1-1.5H4L3 5z M3 6h6l1 5H2z"/></svg>0800 555 019</li>
        <li><svg viewBox="0 0 12 12"><rect x="3" y="0.5" width="6" height="11" rx="1"/><rect x="4" y="2" width="4" height="6" fill="#fff"/></svg>+64 21 555 0147</li>
        <li><svg viewBox="0 0 12 12"><rect x="0.5" y="2" width="11" height="8" rx="1"/><path d="M1 2.5l5 4 5-4" fill="none" stroke="#fff" stroke-width="1"/></svg>derek@harrowcollective.example.nz</li>
        <li><svg viewBox="0 0 12 12"><circle cx="6" cy="6" r="5.5"/><path d="M0.5 6h11M6 0.5c-3 3-3 8 0 11M6 0.5c3 3 3 8 0 11" fill="none" stroke="#fff" stroke-width=".8"/></svg>harrowcollective.example.nz</li>
      </ul>
    </div>
  </section>
</main>
</body>
</html>
```